Valdora Business Card Design - Professional Flexible and forward thinking. Clean and Easy to follow

Management Consulting Company. I focus on business development and concept and operational review. I need a progressive, simple and professional layout design for the business cards, letterhead and envelops
Professional Flexible and forward thinking. Clean and Easy to follow
Mature Business persons and professionals and Corporations

Target Market(s)

Mature Business persons and professionals and Corporations - Government org.

Industry/Entity Type

Consulting

Contact Information for Business Card

Requirements
Must have
• Marcus Valdora
• President
• Phone - 516.382.6047
• email - Mvaldora@valdorapartners.com
• Skype - Marc.valdora
• 7215 Pellham Avenue
• Suite B
• Harrowgate, N.Y. 11904
• USA
Nice to have
• www.valdorapartners.com
Should not have
• N/A

```html
<!DOCTYPE html>
<html lang="en">
<head>
<meta charset="utf-8">
<title>Valdora Associates – Business Card</title>
<link rel="stylesheet" href="https://fonts.googleapis.com/css2?family=Marcellus&family=Marcellus+SC&family=Tenor+Sans&display=swap">
<style>
  :root {
    --ink: #000000;
    --paper: #ffffff;
    --bg: #5a5a5a;
    --orange-deep: #ef5a2a;
    --orange-mid: #f4812f;
    --orange-light: #fdb140;
    --text-soft: #d9d9d9;
  }
  * { margin: 0; padding: 0; box-sizing: border-box; }
  html, body { width: 1200px; height: 1200px; overflow: hidden; }
  body { background: var(--bg); position: relative; font-family: "Tenor Sans", sans-serif; }

  .card { position: absolute; left: 222px; width: 758px; height: 428px; box-shadow: 0 6px 14px rgba(0,0,0,.45); overflow: hidden; }
  .card-front { top: 124px; background: var(--ink); }
  .card-back { top: 648px; height: 430px;
    background: linear-gradient(35deg, var(--orange-deep) 25%, var(--orange-mid) 55%, var(--orange-light) 90%); }

  .brand-square { position: absolute; width: 88px; height: 118px; left: 33px; top: 0;
    background: linear-gradient(160deg, var(--orange-light), var(--orange-deep) 70%); }
  .brand-name { position: absolute; font-family: "Marcellus", serif; font-size: 56px; line-height: 1; white-space: nowrap; }
  .card-front .brand-name { left: 140px; top: 56px; color: var(--paper); }

  .person { position: absolute; left: 34px; top: 180px; }
  .person-name { font-family: "Marcellus SC", serif; font-size: 38px; color: var(--orange-deep); line-height: 1; letter-spacing: 1px; }
  .person-title { font-family: "Marcellus", serif; font-size: 21px; color: var(--text-soft); letter-spacing: 1.5px; margin-top: 2px; }

  .address { position: absolute; left: 34px; top: 278px; color: var(--text-soft); font-size: 18.5px; line-height: 25.5px; }
  .contact { position: absolute; left: 328px; top: 278px; list-style: none; color: var(--text-soft); font-size: 18.5px; line-height: 25.5px; }
  .contact li { display: flex; align-items: center; }
  .contact svg { width: 24px; height: 20px; margin-right: 14px; flex: none; }

  .footer-band { position: absolute; left: 0; top: 0; width: 758px; height: 428px; }
  .website { position: absolute; left: 365px; top: 387px; color: var(--paper); font-family: "Marcellus", serif; font-size: 25px; letter-spacing: .5px; }

  .card-back .brand-square { left: 96px; top: 171px; width: 88px; height: 88px; background: var(--ink); }
  .card-back .brand-name { left: 202px; top: 193px; color: var(--ink); }
</style>
</head>
<body>
  <section class="card card-front">
    <div class="brand-square"></div>
    <div class="brand-name">Valdora Associates</div>

    <div class="person">
      <div class="person-name">Marcus Valdora</div>
      <div class="person-title">PRESIDENT</div>
    </div>

    <div class="address">
      7215 Pellham Avenue<br>Suite B<br>Harrowgate, N.Y. 11904<br>USA
    </div>

    <ul class="contact">
      <li>
        <svg viewBox="0 0 24 20" aria-hidden="true"><path d="M1 7 Q12 -1 23 7 L20 10 L17 7 L7 7 L4 10 Z" fill="#d9d9d9"/><path d="M5 10 L19 10 L21 19 L3 19 Z" fill="#d9d9d9"/><circle cx="12" cy="14" r="3" fill="#000"/></svg>
        516.382.6047
      </li>
      <li>
        <svg viewBox="0 0 24 20" aria-hidden="true"><rect x="1" y="4" width="22" height="14" fill="#d9d9d9"/><path d="M1 4 L12 12 L23 4 M1 18 L9 10 M23 18 L15 10" stroke="#000" stroke-width="1.5" fill="none"/></svg>
        Mvaldora@valdorapartners.com
      </li>
      <li>
        <svg viewBox="0 0 24 20" aria-hidden="true"><circle cx="12" cy="10" r="9" fill="#d9d9d9"/></svg>
        Marc.valdora
      </li>
    </ul>

    <svg class="footer-band" viewBox="0 0 758 428" aria-hidden="true">
      <defs>
        <linearGradient id="bandFill" x1="0" x2="1" y1="0" y2="0">
          <stop offset="0" stop-color="#fdb140"/>
          <stop offset=".45" stop-color="#ef5a2a"/>
          <stop offset="1" stop-color="#ef5a2a"/>
        </linearGradient>
      </defs>
      <path d="M0 414 L312 414 L354 386 L758 386 L758 428 L0 428 Z" fill="url(#bandFill)"/>
      <polyline points="0,406 307,406 350,380 758,380" fill="none" stroke="#ffffff" stroke-width="4"/>
    </svg>
    <div class="website">www.valdorapartners.com</div>
  </section>

  <section class="card card-back">
    <div class="brand-square"></div>
    <div class="brand-name">Valdora Associates</div>
  </section>
</body>
</html>
```